Placing my newer logo on my existing business card

I have a business card that I had you guys do years ago, then I changed my logo, I love both my business card and my logo. The challenge is both my logo and my business card are very similar in color. So I'm not sure how to make my logo stand out.

Sick

```html
<!DOCTYPE html>
<html lang="en">
<head>
<meta charset="utf-8">
<title>Northridge Wellness &amp; Hormone Clinic – Business Card</title>
<link href="https://fonts.googleapis.com/css2?family=Cinzel:wght@500;600&family=Crimson+Text:wght@400;600;700&display=swap" rel="stylesheet">
<style>
  :root {
    --bg: #d4d4d4;
    --card: #ffffff;
    --teal: #86a7aa;
    --teal-text: #74999d;
    --rust: #b0472d;
    --white: #ffffff;
  }
  * { box-sizing: border-box; margin: 0; padding: 0; }
  html, body { width: 1095px; height: 1200px; overflow: hidden; }
  body {
    background: var(--bg);
    font-family: "Crimson Text", Georgia, serif;
    position: relative;
  }
  .card {
    position: absolute;
    left: 107px;
    width: 880px;
    height: 503px;
    background: var(--card);
    box-shadow: 0 6px 18px rgba(0,0,0,0.18);
    overflow: hidden;
  }
  .card--front { top: 64px; }
  .card--back { top: 633px; }

  /* Front */
  .brand {
    position: absolute; top: 40px; left: 0; right: 0;
    text-align: center;
  }
  .brand__dot {
    width: 70px; height: 70px; border-radius: 50%;
    background: var(--teal); margin: 0 auto 22px;
  }
  .brand__name {
    font-family: "Cinzel", "Times New Roman", serif;
    font-weight: 500; color: var(--rust);
    font-size: 30px; line-height: 34px; letter-spacing: 2px;
  }
  .holder {
    position: absolute; top: 238px; left: 0; right: 0; text-align: center;
  }
  .holder__name {
    display: inline-block; background: var(--rust); color: var(--white);
    font-family: "Cinzel", "Times New Roman", serif; font-weight: 600;
    font-size: 31px; line-height: 40px; padding: 0 14px; letter-spacing: 1px;
  }
  .holder__role { color: var(--teal-text); font-size: 27px; line-height: 36px; margin-top: 2px; }
  .contact-band {
    position: absolute; top: 347px; left: 0; right: 0; height: 72px;
    background: var(--teal); color: var(--white); font-size: 20px;
  }
  .contact-band__row { position: absolute; display: flex; align-items: center; gap: 8px; }
  .contact-band svg { width: 14px; height: 14px; fill: var(--white); }
  .address {
    position: absolute; top: 452px; left: 0; right: 0; text-align: center;
    color: var(--rust); font-size: 21px;
    display: flex; justify-content: center; align-items: center; gap: 8px;
  }
  .address svg { width: 12px; height: 16px; fill: var(--rust); }
  .rule-bottom { position: absolute; bottom: 0; left: 0; right: 0; height: 8px; background: var(--rust); }

  /* Back */
  .rule-top { position: absolute; top: 0; left: 0; right: 0; height: 7px; background: var(--rust); }
  .conditions__title {
    position: absolute; top: 14px; left: 78px; right: 78px;
    text-align: center; color: var(--rust); font-weight: 600;
    font-size: 34px; letter-spacing: 0.5px; line-height: 48px;
    border-bottom: 2px solid var(--rust);
  }
  .conditions__col { position: absolute; top: 82px; list-style: none; }
  .conditions__col--left { left: 100px; }
  .conditions__col--right { left: 580px; }
  .conditions__col li {
    color: var(--teal-text); font-weight: 700; font-size: 17px; line-height: 30px;
    padding-left: 22px; position: relative;
  }
  .conditions__col li::before {
    content: "•"; position: absolute; left: 0; color: var(--teal-text);
  }
  .conditions__col li.gap { margin-top: 22px; }
  .conditions__col li.wrap { line-height: 20px; margin-top: 6px; }
  .cta-band {
    position: absolute; left: 0; right: 0; bottom: 0; height: 57px;
    background: var(--teal); color: var(--white); display: flex; align-items: center;
  }
  .cta-band__call { width: 440px; padding-left: 36px; font-size: 30px; font-weight: 600; }
  .cta-band__divider { width: 4px; height: 100%; background: var(--white); }
  .cta-band__web { flex: 1; text-align: center; font-size: 23px; font-weight: 600; }
</style>
</head>
<body>

<section class="card card--front" aria-label="Business card front">
  <div class="brand">
    <div class="brand__dot"></div>
    <div class="brand__name">Northridge Wellness<br>&amp; Hormone Clinic</div>
  </div>
  <div class="holder">
    <div class="holder__name">Dana Whitfield</div>
    <div class="holder__role">Director</div>
  </div>
  <div class="contact-band">
    <div class="contact-band__row" style="left:220px; top:10px;">
      <svg viewBox="0 0 24 24"><path d="M6.6 10.8a15 15 0 0 0 6.6 6.6l2.2-2.2c.3-.3.7-.4 1-.2 1.1.4 2.3.6 3.6.6.6 0 1 .4 1 1V20c0 .6-.4 1-1 1A17 17 0 0 1 3 4c0-.6.4-1 1-1h3.5c.6 0 1 .4 1 1 0 1.3.2 2.5.6 3.6.1.3 0 .7-.2 1z"/></svg>
      <span>(555) 201-4410</span>
    </div>
    <div class="contact-band__row" style="left:480px; top:10px;">
      <svg viewBox="0 0 24 24"><path d="M6 2h12v6H6zM3 9h18v9h-3v4H6v-4H3zm5 6v5h8v-5z"/></svg>
      <span>(555) 201-4411</span>
    </div>
    <div class="contact-band__row" style="left:0; right:0; top:38px; justify-content:center;">
      <span>• northridgewellness.com</span>
    </div>
  </div>
  <div class="address">
    <svg viewBox="0 0 12 16"><path d="M6 0a6 6 0 0 0-6 6c0 4.5 6 10 6 10s6-5.5 6-10a6 6 0 0 0-6-6zm0 8.5A2.5 2.5 0 1 1 6 3.5a2.5 2.5 0 0 1 0 5z"/></svg>
    <span>1280 Cedar Row Ste 4, Fairview 00000</span>
  </div>
  <div class="rule-bottom"></div>
</section>

<section class="card card--back" aria-label="Business card back">
  <div class="rule-top"></div>
  <h2 class="conditions__title">Conditions we address for women and men</h2>
  <ul class="conditions__col conditions__col--left">
    <li>PCOS</li>
    <li>Hysterectomy</li>
    <li>Type-II Diabetes</li>
    <li>Insulin Resistance</li>
    <li>Hypothyroid</li>
    <li class="gap">Underactive Thyroid</li>
    <li>Fibromyalgia</li>
    <li>Chronic Fatigue</li>
    <li>Chronic Headaches &amp; Migraines</li>
    <li>Hypertension</li>
    <li>Elevated Fasting Glucose</li>
  </ul>
  <ul class="conditions__col conditions__col--right">
    <li>Pre-Diabetes</li>
    <li>Abdominal Obesity</li>
    <li>High Triglycerides</li>
    <li>High Blood Pressure</li>
    <li>High Cholesterol</li>
    <li class="gap">Gestational Diabetes</li>
    <li>Epstein Barr</li>
    <li>Infertility</li>
    <li>Infertility Drugs</li>
    <li class="wrap">Anti-Depression<br>Medications</li>
  </ul>
  <div class="cta-band">
    <div class="cta-band__call">Call Today!: (555) 201-4410</div>
    <div class="cta-band__divider"></div>
    <div class="cta-band__web">www.northridgewellness.com</div>
  </div>
</section>

</body>
</html>
```